Website update for Mobile lighting company

We are looking to get a fresh look to our website and update it with some new products and services we are just starting to offer. We host there website through site nest and use there website builder so we would like comparable files. The pages we would want are:
Home page
VEXA (one of our light tower units)
KR62 (one of our light tower units)
KR38 (one of our light tower units)
KR14 (one of our light tower units)
Service Page (would describe different serves we provide)
Contact Page with a google map
We would like to stick with our company colours and keep it clean and modern looking. Current website is www.brindlepowr.ca

```html
<!DOCTYPE html>
<html lang="en">
<head>
<meta charset="utf-8">
<title>Brindle Power Services Corp.</title>
<link href="https://fonts.googleapis.com/css2?family=Roboto:wght@300;400;500;700&display=swap" rel="stylesheet">
<style>
:root{
  --accent:#c2d000;
  --navy:#1f3b63;
  --ink:#2c2c2c;
  --grey:#777;
  --light:#f2f2f2;
  --nav:#1c1c1c;
  --footer:#242424;
  --footer-base:#1a1a1a;
  --band:#2d4f80;
}
*{margin:0;padding:0;box-sizing:border-box}
html,body{width:723px;height:1200px;overflow:hidden}
body{position:relative;background:#fff;font-family:'Roboto',sans-serif;color:var(--ink)}
.abs{position:absolute}

.site-header{top:0;left:0;width:723px;height:55px;background:#fff}
.brand{left:0;width:723px;top:12px;display:flex;justify-content:center;align-items:center;gap:8px}
.brand-dot{width:26px;height:26px;border-radius:50%;background:var(--navy)}
.brand-name{font-size:17px;font-weight:700;color:var(--navy);letter-spacing:.5px}

.main-nav{top:55px;left:0;width:723px;height:23px;background:var(--nav)}
.main-nav ul{list-style:none;display:flex;justify-content:center;gap:26px;height:23px;align-items:center;padding-right:90px}
.main-nav li{font-size:6.5px;letter-spacing:.6px;color:#8a8a8a;text-transform:uppercase}
.main-nav li.current{color:var(--accent)}

.hero-photo{left:98px;top:99px;width:528px;height:248px;background:linear-gradient(180deg,#6e7479 0%,#a7a8a3 45%,#55595a 100%)}

.intro{top:374px;left:0;width:723px;text-align:center}
.intro h1{font-size:16px;font-weight:400;letter-spacing:.5px;color:#222}
.intro p{margin-top:8px;font-size:13px;font-weight:300;line-height:18px;color:#555}

.solution{top:459px;left:0;width:723px;height:198px;background:var(--light)}
.section-title{font-size:10px;font-weight:700;color:var(--accent);letter-spacing:.3px}
.solution .section-title{left:98px;top:20px}
.feature{width:165px}
.feature svg{position:absolute;left:0;top:0}
.feature h3{margin-left:18px;font-size:7px;font-weight:700;color:var(--navy)}
.feature p{margin:5px 0 0 18px;font-size:6px;line-height:9.5px;color:var(--grey)}

.testimonials{top:657px;left:0;width:723px;height:166px;background:linear-gradient(180deg,#3a5d8e 0%,var(--band) 55%,#23406a 100%)}
.testimonials .kicker{top:38px;width:723px;text-align:center;font-size:6.5px;color:var(--accent);letter-spacing:.4px}
.testimonials blockquote{top:56px;left:161px;width:400px;text-align:center;font-size:8.5px;line-height:17px;color:#d7dfec}
.testimonials cite{top:94px;width:723px;text-align:center;font-style:normal;font-size:5.5px;color:var(--accent);letter-spacing:.5px}

.about .section-title{left:98px;top:827px}
.about-photo{left:98px;top:849px;width:88px;height:126px;background:linear-gradient(180deg,#0c1a2e 0%,#1f2e44 60%,#5a5f62 100%)}
.about-copy{left:192px;top:847px;width:162px;font-size:6.5px;line-height:10px;color:#444}
.about-copy p+p{margin-top:5px;font-size:5.8px;line-height:8.5px;color:var(--grey)}

.services .section-title{left:368px;top:827px}
.service{left:372px;width:240px}
.service svg{position:absolute;left:0;top:0}
.service h4{margin-left:27px;font-size:7px;font-weight:700;color:var(--navy)}
.service p{margin:4px 0 0 27px;font-size:5.8px;line-height:8.5px;color:var(--grey)}

.site-footer{top:998px;left:0;width:723px;height:160px;background:var(--footer);text-align:center}
.site-footer h2{margin-top:31px;font-size:7px;font-weight:500;color:var(--accent);letter-spacing:.5px}
.site-footer .lede{margin:9px auto 0;width:360px;font-size:6px;line-height:11px;color:#bbb}
.social{margin-top:14px;display:flex;justify-content:center;gap:5px}
.social span{width:13px;height:13px;border-radius:50%;border:1.5px solid}
.contact-line{margin-top:14px;font-size:5.8px;color:#bbb;letter-spacing:.2px}
.copyright{top:1158px;left:0;width:723px;height:42px;background:var(--footer-base);text-align:center;line-height:42px;font-size:6.5px;color:#999}
</style>
</head>
<body>

<header class="site-header abs">
  <div class="brand abs">
    <span class="brand-dot"></span>
    <span class="brand-name">Brindle Power Services Corp.</span>
  </div>
</header>

<nav class="main-nav abs">
  <ul>
    <li class="current">Home</li>
    <li>About us</li>
    <li>VEXA</li>
    <li>Products</li>
    <li>Services</li>
    <li>Benefits</li>
    <li>Contact</li>
  </ul>
</nav>

<div class="hero-photo abs" role="img" aria-label="Workshop photo of a rack of VEXA crown mount LED light heads on a stand"></div>

<section class="intro abs">
  <h1>LIGHTING SYSTEMS FOR THE FUTURE</h1>
  <p>The VEXA CROWN MOUNT lighting system (patent pending) combines a sophisticated,<br>yet obvious design with the latest technology to bring not only a safer solution for illumination</p>
</section>

<section class="solution abs">
  <h2 class="section-title abs">OUR SOLUTION</h2>

  <div class="feature abs" style="left:7px;top:56px">
    <svg width="12" height="14" viewBox="0 0 12 14"><path d="M6 1v8M3 4l3-3 3 3M2 12h8" stroke="#1f3b63" stroke-width="1.3" fill="none"/></svg>
    <h3>A self contained unit</h3>
    <p>Tower, mast, power and lamps ship as one frame, ready to run the day it lands on site.</p>
  </div>
  <div class="feature abs" style="left:187px;top:56px">
    <svg width="12" height="14" viewBox="0 0 12 14"><circle cx="6" cy="5" r="4" stroke="#1f3b63" stroke-width="1.3" fill="none"/><path d="M4 11h4M4.5 13h3" stroke="#1f3b63" stroke-width="1.3"/></svg>
    <h3>Environmental benefits</h3>
    <p>Lower fuel draw and quiet running cut noise, fumes and waste on every job we light.</p>
  </div>
  <div class="feature abs" style="left:367px;top:56px">
    <svg width="12" height="14" viewBox="0 0 12 14"><path d="M3 1v4M9 1v4M2 5h8v3a4 4 0 0 1-8 0zM6 12v2" stroke="#1f3b63" stroke-width="1.3" fill="none"/></svg>
    <h3>Easy to install</h3>
    <p>The crown mount drops onto the mast in minutes with simple hand tools and one crew.</p>
  </div>
  <div class="feature abs" style="left:7px;top:126px">
    <svg width="12" height="14" viewBox="0 0 12 14"><path d="M6 1l5 2v4c0 3-2 5-5 6-3-1-5-3-5-6V3z" fill="#1f3b63"/></svg>
    <h3>Better overall safety</h3>
    <p>Even, glare free light across the pad helps crews see hazards sooner on night shifts.</p>
  </div>
  <div class="feature abs" style="left:187px;top:126px">
    <svg width="12" height="14" viewBox="0 0 12 14"><rect x="1" y="2" width="10" height="8" rx="1" stroke="#1f3b63" stroke-width="1.3" fill="none"/><path d="M4 12h4" stroke="#1f3b63" stroke-width="1.3"/></svg>
    <h3>LED Light Technology</h3>
    <p>Long life LED heads give bright output with a fraction of the power of old lamps.</p>
  </div>
  <div class="feature abs" style="left:367px;top:126px">
    <svg width="12" height="14" viewBox="0 0 12 14"><circle cx="6" cy="7" r="5" fill="#1f3b63"/><path d="M4 7h4M6 5l2 2-2 2" stroke="#fff" stroke-width="1" fill="none"/></svg>
    <h3>Renewable energy</h3>
    <p>Solar and hybrid options keep the tower running longer between every refuel stop.</p>
  </div>
</section>

<section class="testimonials abs" role="img" aria-label="Blue tinted photo of light heads behind a customer quote">
  <p class="kicker abs">WHAT OUR CUSTOMERS THINK -</p>
  <blockquote class="abs">Cras justo odio, dapibus ac facilisis in, egestas eget quam. Maecenas faucibus mollis interdum. Vivamus sagittis lacus vel augue laoreet rutrum faucibus dolor auctor gravida at eget metus.</blockquote>
  <cite class="abs">DARLA MORTON</cite>
</section>

<section class="about">
  <h2 class="section-title abs">A LITTLE ABOUT ME</h2>
  <div class="about-photo abs" role="img" aria-label="Night photo of a light tower shining over a yard"></div>
  <div class="about-copy abs">
    <p>Here at BRINDLE POWER SERVICES CORP, we are dedicated to innovation. Sometimes the biggest ideas come from the simplest of ideas or that the best solutions evolve from the curiosity of one person.</p>
    <p>Our team has over 20 years of experience in a multitude of levels with a diverse group of companies, we have learned that truly successful innovation stems from the needs of everyday. With the VEXA Crown Mount we recognized that there must be a better way, so we built it.</p>
  </div>
</section>

<section class="services">
  <h2 class="section-title abs">MY SERVICES</h2>
  <div class="service abs" style="top:848px">
    <svg width="12" height="14" viewBox="0 0 12 14"><rect x="1" y="2" width="10" height="10" rx="1" fill="#1f3b63"/><path d="M6 4v6M4 6h4" stroke="#fff" stroke-width="1"/></svg>
    <h4>Cost savings</h4>
    <p>Lower fuel, fewer service calls and longer lamp life bring real<br>savings to each project across the full rental term.</p>
  </div>
  <div class="service abs" style="top:893px">
    <svg width="12" height="14" viewBox="0 0 12 14"><path d="M2 2h8v5l-4 5-4-5z" fill="#1f3b63"/></svg>
    <h4>Added HSE Benefits</h4>
    <p>Better sight lines and less noise support safer crews and<br>cleaner audits on every site we help to light up.</p>
  </div>
  <div class="service abs" style="top:937px">
    <svg width="12" height="14" viewBox="0 0 12 14"><path d="M2 12C2 5 6 2 11 2c0 6-3 10-9 10zM2 12l6-6" stroke="#1f3b63" stroke-width="1.3" fill="#1f3b63"/></svg>
    <h4>Environmentally beneficial</h4>
    <p>Hybrid power and efficient heads reduce emissions while<br>keeping the same bright coverage through the night.</p>
  </div>
</section>

<footer class="site-footer abs">
  <h2>- GET IN TOUCH WITH US -</h2>
  <p class="lede">Call or write to our team to book a tower, ask about a unit or plan lighting for your next project. We reply within one business day.</p>
  <div class="social">
    <span style="border-color:#e0802a"></span>
    <span style="border-color:#3b6fb5"></span>
    <span style="border-color:#2f9bd6"></span>
    <span style="border-color:#a44c8e"></span>
    <span style="border-color:#d23c2c"></span>
  </div>
  <p class="contact-line">#4, 18 Ridgeview Way NE, Calgary, Alberta T2X 0B1 &nbsp;/&nbsp; T. +1 (403) 555-0147 &nbsp;/&nbsp; info@brindlepowerservices.ca</p>
</footer>

<div class="copyright abs">© 2015 Brindle Power Services Corp. All rights reserved.</div>

</body>
</html>
```